Looking for a modern website banner design

Bramblecrest Coaching Partners looking for the development of the main banner of the website. The project description and photos are included in the upload files.

```html
<!DOCTYPE html>
<html lang="en">
<head>
<meta charset="utf-8">
<title>Bramblecrest Coaching Partners – Testimonial Banner</title>
<link href="https://fonts.googleapis.com/css2?family=Barlow:wght@400;700&family=Barlow+Semi+Condensed:wght@600&display=swap" rel="stylesheet">
<style>
  :root {
    --brand-blue: #1274bd;
    --slate-grey: #6a6a6a;
    --quote-mark: #8cbde6;
    --text-white: #ffffff;
    --caption-blue: #9ccbf0;
    --photo-dark: #1d2230;
    --photo-red: #b8323b;
  }
  html, body {
    margin: 0;
    padding: 0;
    overflow: hidden;
  }
  .banner {
    position: relative;
    width: 1200px;
    height: 562px;
    overflow: hidden;
    background: var(--brand-blue);
    font-family: "Barlow", Arial, sans-serif;
  }
  .banner__corner {
    position: absolute;
    inset: 0;
  }
  .testimonial-photo {
    position: absolute;
    left: 0;
    top: 0;
    filter: drop-shadow(0 6px 14px rgba(0,0,0,0.25));
  }
  .quote-mark {
    position: absolute;
    fill: var(--quote-mark);
  }
  .quote-mark--open {
    left: 550px;
    top: 102px;
  }
  .testimonial-quote {
    position: absolute;
    left: 608px;
    top: 113px;
    margin: 0;
    color: var(--text-white);
    font-weight: 700;
    font-size: 23.5px;
    line-height: 33.2px;
    letter-spacing: -0.1px;
    white-space: nowrap;
  }
  .quote-mark--close {
    display: inline-block;
    vertical-align: -10px;
    margin-left: 8px;
  }
  .attribution__rule {
    position: absolute;
    left: 608px;
    top: 345px;
    width: 36px;
    height: 2px;
    background: var(--text-white);
  }
  .attribution__name {
    position: absolute;
    left: 608px;
    top: 374px;
    margin: 0;
    color: var(--text-white);
    font-family: "Barlow Semi Condensed", Arial, sans-serif;
    font-weight: 600;
    font-size: 23px;
  }
  .attribution__team {
    position: absolute;
    left: 608px;
    top: 406px;
    margin: 0;
    color: var(--caption-blue);
    font-size: 17.5px;
    line-height: 27px;
  }
</style>
</head>
<body>
<div class="banner">
  <svg class="banner__corner" width="1200" height="562" viewBox="0 0 1200 562" aria-hidden="true">
    <polygon points="0,0 559,0 0,562" fill="var(--slate-grey)"/>
  </svg>

  <svg class="testimonial-photo" width="1200" height="562" viewBox="0 0 1200 562" role="img" aria-label="Photo of a smiling professional hockey player in team jersey and helmet, raising his stick on the way to the ice">
    <defs>
      <linearGradient id="photoTones" x1="0" y1="0" x2="1" y2="1">
        <stop offset="0" stop-color="#3a3128"/>
        <stop offset="0.45" stop-color="var(--photo-dark)"/>
        <stop offset="0.75" stop-color="var(--photo-red)"/>
        <stop offset="1" stop-color="#141414"/>
      </linearGradient>
    </defs>
    <path d="M156,72 H433 Q464,72 464,103 V440 C464,482 428,516 361,536 L334,481 C380,460 395,440 395,412 H156 Q125,412 125,381 V103 Q125,72 156,72 Z" fill="url(#photoTones)"/>
  </svg>

  <svg class="quote-mark quote-mark--open" width="52" height="30" viewBox="0 0 52 30" aria-hidden="true">
    <path d="M12,30 A12,12 0 1 1 12,6 C12,2 15,0 19,0 C15,2 14,4 14,6 A12,12 0 0 1 12,30 Z"/>
    <path d="M39,30 A12,12 0 1 1 39,6 C39,2 42,0 46,0 C42,2 41,4 41,6 A12,12 0 0 1 39,30 Z"/>
  </svg>

  <p class="testimonial-quote">
    Bramblecrest has provided support that has<br>
    allowed me to develop as a person and<br>
    an athlete.&nbsp; The S.T.R.I.D.E.™ process allowed<br>
    me to stay focused on attainable goals each<br>
    season and progress from Junior to College<br>
    and now Professional Hockey.<svg class="quote-mark quote-mark--close" width="52" height="30" viewBox="0 0 52 30" aria-hidden="true"><path d="M13,0 A12,12 0 1 1 13,24 C13,28 10,30 6,30 C10,28 11,26 11,24 A12,12 0 0 1 13,0 Z"/><path d="M40,0 A12,12 0 1 1 40,24 C40,28 37,30 33,30 C37,28 38,26 38,24 A12,12 0 0 1 40,0 Z"/></svg>
  </p>

  <div class="attribution__rule"></div>
  <h2 class="attribution__name">Marcus Delorme</h2>
  <p class="attribution__team">Riverton Comets<br>Atlantic Pro Hockey League</p>
</div>
</body>
</html>
```